Valmora Holdings - Tidal Crest Car Wash automatic car wash signage

We are wanting to have a new automatic car wash sign designed. Our current one is dated and there are numerous options that are no longer available. We like the look of a clean sharp design in keeping with the Tidal Crest colours; orange and blues. The sign should have the Ultimate and Premium options, the "Tidal Crest" and Tidal Crest Car Wash designed in a clean, concise and cool manner.

Font styles to use
Sans Serif

Colors
f37122
3276b5
0255a3
34a7d8

Requirements
Must have
• This project must have the Ultimate and Premium options, the "bucket" and the Tidal Crest Car Wash title. The orange is a key colour with blues for water.

```html
<!DOCTYPE html>
<html lang="en">
<head>
<meta charset="utf-8">
<title>Tidal Crest Car Wash – Wash Menu Sign</title>
<link rel="stylesheet" href="https://fonts.googleapis.com/css2?family=Montserrat:wght@700;800&family=Poppins:ital,wght@1,800&family=Fira+Sans+Condensed:wght@600&display=swap">
<style>
  :root {
    --orange-light: #ec8b44;
    --orange: #f37122;
    --orange-deep: #c63f2c;
    --blue-deep: #2e3a9c;
    --blue-mid: #3a4fb0;
    --violet: #6a3aa0;
    --header-blue: #2b3aa0;
    --white: #ffffff;
    --page: #eef1f5;
  }
  * { margin: 0; padding: 0; box-sizing: border-box; }
  html, body { width: 1200px; height: 970px; overflow: hidden; background: var(--page); }
  .sign {
    position: absolute; left: 12px; top: 181px;
    width: 1176px; height: 608px; overflow: hidden;
    background: linear-gradient(90deg, var(--orange-light) 0%, var(--orange) 45%, var(--orange-deep) 100%);
  }
  .water-band { position: absolute; inset: 0; }
  .sign-title {
    position: absolute; left: 0; right: 0; top: 24px; text-align: center;
    font-family: "Poppins", sans-serif; font-style: italic; font-weight: 800;
    font-size: 92px; letter-spacing: -2px; color: var(--white);
    text-shadow: 3px 3px 0 rgba(120, 40, 20, .45);
  }
  .feature-list { position: absolute; left: 114px; top: 194px; width: 554px; list-style: none; }
  .feature-list li {
    height: 37.8px; line-height: 37px;
    font-family: "Montserrat", sans-serif; font-weight: 800; font-size: 24.5px;
    color: var(--white); text-shadow: 2px 2px 2px rgba(10, 10, 60, .55);
    border-bottom: 1px solid rgba(255,255,255,.75);
  }
  .feature-list li:last-child { border-bottom: none; }
  .package { position: absolute; top: 144px; width: 190px; }
  .package--ultimate { left: 683px; }
  .package--premium { left: 898px; }
  .package-name {
    height: 50px; margin: 0 4px; border-radius: 12px 12px 0 0;
    background: var(--header-blue); color: var(--white);
    font-family: "Fira Sans Condensed", sans-serif; font-weight: 600; font-size: 29px;
    text-align: center; line-height: 48px;
  }
  .package-rows {
    list-style: none; border: 4px solid var(--white); border-radius: 18px; overflow: hidden;
    background: linear-gradient(90deg, var(--orange-light), var(--orange-deep));
  }
  .package-rows li {
    height: 38px; display: flex; align-items: center; justify-content: center;
    border-bottom: 1.5px solid var(--white);
  }
  .package-rows li:last-child { border-bottom: none; }
  .tick { width: 30px; height: 24px; }
</style>
</head>
<body>
<main class="sign">
  <svg class="water-band" viewBox="0 0 1176 608" width="1176" height="608" role="img" aria-label="Blue water background with soapy bubbles">
    <defs>
      <linearGradient id="water" x1="0" y1="0" x2="1" y2="1">
        <stop offset="0" stop-color="#5a6cc8"/>
        <stop offset="0.35" stop-color="#3a48b0"/>
        <stop offset="0.75" stop-color="#2e3a9c"/>
        <stop offset="1" stop-color="#6a3aa0"/>
      </linearGradient>
    </defs>
    <path d="M0,190 Q330,118 690,222 L880,318 C905,400 920,520 932,608 L0,608 Z" fill="url(#water)"/>
    <path d="M0,184 Q330,112 690,216 L882,312" fill="none" stroke="#ffffff" stroke-width="14"/>
    <path d="M0,170 Q330,98 690,202" fill="none" stroke="#2e3a9c" stroke-width="6"/>
  </svg>

  <h1 class="sign-title">TIDAL CREST CAR WASH</h1>

  <ul class="feature-list">
    <li>Windshield &amp; Front End Bug Wash</li>
    <li>Under Carriage &amp; Wheel Blaster</li>
    <li>Extra Pass Of High Pressure Wash</li>
    <li>Try Foam Conditioner / Cleaner</li>
    <li>Side Kick Dryers</li>
    <li>Wax/surface Protectant</li>
    <li>On Board Overhead Dryer</li>
    <li>Two Passes Of Pre-soak</li>
    <li>High Pressure Wash Pass</li>
    <li>Spot Free Rimse</li>
  </ul>

  <section class="package package--ultimate">
    <h2 class="package-name">Ultimate $14</h2>
    <ul class="package-rows">
      <li><svg class="tick" viewBox="0 0 30 24"><path d="M4,14 L11,21 L27,3" fill="none" stroke="#fff" stroke-width="2"/></svg></li>
      <li><svg class="tick" viewBox="0 0 30 24"><path d="M4,14 L11,21 L27,3" fill="none" stroke="#fff" stroke-width="2"/></svg></li>
      <li><svg class="tick" viewBox="0 0 30 24"><path d="M4,14 L11,21 L27,3" fill="none" stroke="#fff" stroke-width="2"/></svg></li>
      <li><svg class="tick" viewBox="0 0 30 24"><path d="M4,14 L11,21 L27,3" fill="none" stroke="#fff" stroke-width="2"/></svg></li>
      <li><svg class="tick" viewBox="0 0 30 24"><path d="M4,14 L11,21 L27,3" fill="none" stroke="#fff" stroke-width="2"/></svg></li>
      <li><svg class="tick" viewBox="0 0 30 24"><path d="M4,14 L11,21 L27,3" fill="none" stroke="#fff" stroke-width="2"/></svg></li>
      <li><svg class="tick" viewBox="0 0 30 24"><path d="M4,14 L11,21 L27,3" fill="none" stroke="#fff" stroke-width="2"/></svg></li>
      <li><svg class="tick" viewBox="0 0 30 24"><path d="M4,14 L11,21 L27,3" fill="none" stroke="#fff" stroke-width="2"/></svg></li>
      <li><svg class="tick" viewBox="0 0 30 24"><path d="M4,14 L11,21 L27,3" fill="none" stroke="#fff" stroke-width="2"/></svg></li>
      <li><svg class="tick" viewBox="0 0 30 24"><path d="M4,14 L11,21 L27,3" fill="none" stroke="#fff" stroke-width="2"/></svg></li>
    </ul>
  </section>

  <section class="package package--premium">
    <h2 class="package-name">Premium $12</h2>
    <ul class="package-rows">
      <li></li>
      <li><svg class="tick" viewBox="0 0 30 24"><path d="M4,14 L11,21 L27,3" fill="none" stroke="#fff" stroke-width="2"/></svg></li>
      <li></li>
      <li></li>
      <li><svg class="tick" viewBox="0 0 30 24"><path d="M4,14 L11,21 L27,3" fill="none" stroke="#fff" stroke-width="2"/></svg></li>
      <li></li>
      <li><svg class="tick" viewBox="0 0 30 24"><path d="M4,14 L11,21 L27,3" fill="none" stroke="#fff" stroke-width="2"/></svg></li>
      <li><svg class="tick" viewBox="0 0 30 24"><path d="M4,14 L11,21 L27,3" fill="none" stroke="#fff" stroke-width="2"/></svg></li>
      <li><svg class="tick" viewBox="0 0 30 24"><path d="M4,14 L11,21 L27,3" fill="none" stroke="#fff" stroke-width="2"/></svg></li>
      <li><svg class="tick" viewBox="0 0 30 24"><path d="M4,14 L11,21 L27,3" fill="none" stroke="#fff" stroke-width="2"/></svg></li>
    </ul>
  </section>
</main>
</body>
</html>
```